New Motorcycle Model (Vireo 2019) Poster Design with highlighted features.

Poster : The dimension is 80cm(W) x 120cm(H)
We are a leading company for manufacturing Motorcycles based in Egypt. We 'd like to design a 80x180cm poster to highlight the new enhancements introduced in VIREO model 2019.
If we 'd like to break down the design into different sections will be:
- 2 Company logos (BRUMK & TORVELIN)
- The motorcycle portrait.
- The featured motorcycle parts with some space to write small description for each part.
- Header: MODRENI VIREO 150 (K72) 2019 Features.
- A line for a greetings from the company.
P.S:It's preferred to have the all the text easily editable at the poster because it will be in another Language in the final revision.
Target Market(s)
Economical Motorcycle Buyers
Look and feel
Each slider illustrates characteristics of the customer's brand and the style your logo design should communicate.

```html
<!DOCTYPE html>
<html lang="en">
<head>
<meta charset="utf-8">
<title>Modreni Vireo 150 (K72) 2019 Features</title>
<link rel="stylesheet" href="https://fonts.googleapis.com/css2?family=Bungee&family=Josefin+Sans:wght@300&family=Mr+Dafoe&family=Open+Sans:wght@600&display=swap">
<style>
  :root {
    --bg-dark: #0c0c0c;
    --bg-mid: #2a2a2a;
    --red: #d4252a;
    --red-deep: #8e1014;
    --silver-light: #ffffff;
    --silver-mid: #cfcfcf;
    --silver-dark: #8a8a8a;
    --white: #ffffff;
    --text-body: #f1f1f1;
  }
  * { margin: 0; padding: 0; box-sizing: border-box; }
  html, body { width: 1200px; height: 2699px; overflow: hidden; background: var(--bg-dark); }
  .poster {
    position: relative;
    width: 1200px; height: 2699px;
    overflow: hidden;
    background:
      radial-gradient(ellipse 700px 900px at 50% 1250px, #3a3a3a 0%, rgba(40,40,40,0.6) 45%, rgba(0,0,0,0) 80%),
      linear-gradient(180deg, #1c1c1c 0%, var(--bg-mid) 40%, #151515 75%, var(--bg-dark) 100%);
  }
  .brand-top {
    position: absolute; top: 120px; left: 0; width: 100%;
    display: flex; justify-content: center; align-items: center; gap: 18px;
  }
  .brand-top .mark { width: 44px; height: 44px; border-radius: 50%; background: var(--silver-mid); }
  .brand-name {
    font-family: 'Bungee', sans-serif; font-size: 46px; color: var(--silver-mid); letter-spacing: 2px;
  }
  .headline {
    position: absolute; left: 0; width: 100%; text-align: center;
    font-family: 'Bungee', sans-serif; line-height: 1;
    background: linear-gradient(180deg, var(--silver-light) 0%, var(--silver-light) 35%, var(--silver-dark) 55%, var(--silver-mid) 75%, var(--silver-light) 100%);
    -webkit-background-clip: text; background-clip: text; color: transparent;
    -webkit-text-stroke: 3px var(--red);
  }
  .headline--model { top: 335px; font-size: 178px; letter-spacing: -4px; }
  .headline--series { top: 545px; font-size: 205px; letter-spacing: -2px; }
  .headline--spec { top: 805px; font-size: 124px; letter-spacing: -3px; -webkit-text-stroke: 2px var(--red); }
  .features-label {
    position: absolute; top: 1004px; left: 0; width: 100%;
    display: flex; justify-content: center; align-items: center; gap: 24px;
    font-family: 'Josefin Sans', sans-serif; font-weight: 300; font-size: 52px;
    letter-spacing: 22px; color: var(--white);
  }
  .features-label .rule { display: flex; flex-direction: column; gap: 6px; }
  .features-label .rule span { display: block; width: 36px; height: 3px; background: var(--white); }
  .greeting {
    position: absolute; z-index: 2; top: 1130px; left: 590px; width: 560px;
    font-family: 'Mr Dafoe', cursive; font-size: 88px; line-height: 0.95;
    color: var(--red); white-space: nowrap;
    transform: rotate(-12deg); transform-origin: left top;
  }
  .greeting span { display: block; }
  .greeting span + span { padding-left: 20px; }
  .hero-bike {
    position: absolute; z-index: 1; left: 108px; top: 1300px; width: 980px; height: 500px;
    border-radius: 40px 40px 20px 20px;
    background: radial-gradient(ellipse at 40% 50%, #b5242a 0%, #6b1a1c 35%, #4a4a4a 65%, rgba(30,30,30,0) 100%);
  }
  .feature-grid {
    position: absolute; top: 1908px; left: 72px; width: 1058px;
    display: grid; grid-template-columns: repeat(4, 248px); column-gap: 22px;
  }
  .feature-photo {
    width: 248px; height: 252px; border: 3px solid var(--red);
    background: linear-gradient(160deg, #f2f2f2 0%, #bdbdbd 55%, #7d7d7d 100%);
  }
  .feature-photo--engine { background: linear-gradient(160deg, #e8e8e8 0%, #a9a9a9 55%, #b7262a 100%); }
  .feature-photo--wheel { background: linear-gradient(160deg, #c62a2e 0%, #f4f4f4 35%, #3a3a3a 100%); }
  .feature-photo--gauges { background: linear-gradient(180deg, #d7d7d7 0%, #2e2e2e 55%, #111 100%); }
  .feature-title {
    margin-top: 52px; text-align: center;
    font-family: 'Bungee', sans-serif; font-size: 25px; color: var(--red);
    -webkit-text-stroke: 0.6px var(--white);
  }
  .feature-text {
    margin-top: 14px; padding: 0 4px;
    font-family: 'Open Sans', sans-serif; font-weight: 600; font-size: 15.5px; line-height: 22px;
    color: var(--text-body);
  }
  .brand-bottom {
    position: absolute; top: 2540px; left: 0; width: 100%;
    display: flex; justify-content: center; align-items: center; gap: 14px;
  }
  .brand-bottom .mark { width: 30px; height: 30px; border-radius: 50%; background: var(--red); }
  .brand-bottom .brand-name { font-size: 48px; color: var(--silver-mid); }
</style>
</head>
<body>
<main class="poster">
  <header>
    <div class="brand-top"><span class="mark"></span><span class="brand-name">TORVELIN</span></div>
    <h1>
      <span class="headline headline--model">MODRENI</span>
      <span class="headline headline--series">VIREO</span>
      <span class="headline headline--spec">150 (K72) 2019</span>
    </h1>
    <div class="features-label">
      <span class="rule"><span></span><span></span></span>
      FEATURES
      <span class="rule"><span></span><span></span></span>
    </div>
  </header>

  <p class="greeting"><span>Greetings from</span><span>the company</span></p>

  <div class="hero-bike" role="img" aria-label="Photo of the red Vireo 150 motorcycle, side view"></div>

  <section class="feature-grid">
    <article class="feature">
      <div class="feature-photo feature-photo--engine" role="img" aria-label="Close-up photo of the chrome engine"></div>
      <h2 class="feature-title">CRAS IN TEMPUS</h2>
      <p class="feature-text">Lorem ipsum dolor sit amet, consectetur adipiscing elit. Nullam egestas sem eu congue pretium. Phasellus auctor orci mauris, non viverra tortor eleifend at. Etiam placerat convallis magna, sed porttitor enim consectetur scelerisque. Donec efficitur cursus magna.</p>
    </article>
    <article class="feature">
      <div class="feature-photo feature-photo--wheel" role="img" aria-label="Close-up photo of the front wheel and mudguard"></div>
      <h2 class="feature-title">CRAS IN TEMPUS</h2>
      <p class="feature-text">Lorem ipsum dolor sit amet, consectetur adipiscing elit. Nullam egestas sem eu congue pretium. Phasellus auctor orci mauris, non viverra tortor eleifend at. Etiam placerat convallis magna, sed porttitor enim consectetur scelerisque. Donec efficitur cursus magna.</p>
    </article>
    <article class="feature">
      <div class="feature-photo" role="img" aria-label="Close-up photo of the foot peg and exhaust"></div>
      <h2 class="feature-title">CRAS IN TEMPUS</h2>
      <p class="feature-text">Lorem ipsum dolor sit amet, consectetur adipiscing elit. Nullam egestas sem eu congue pretium. Phasellus auctor orci mauris, non viverra tortor eleifend at. Etiam placerat convallis magna, sed porttitor enim consectetur scelerisque. Donec efficitur cursus magna.</p>
    </article>
    <article class="feature">
      <div class="feature-photo feature-photo--gauges" role="img" aria-label="Close-up photo of the speedometer and ignition"></div>
      <h2 class="feature-title">CRAS IN TEMPUS</h2>
      <p class="feature-text">Lorem ipsum dolor sit amet, consectetur adipiscing elit. Nullam egestas sem eu congue pretium. Phasellus auctor orci mauris, non viverra tortor eleifend at. Etiam placerat convallis magna, sed porttitor enim consectetur scelerisque. Donec efficitur cursus magna.</p>
    </article>
  </section>

  <footer class="brand-bottom"><span class="mark"></span><span class="brand-name">BRUMK</span></footer>
</main>
</body>
</html>
```